Flyer für Veranstaltungstechnik-Unternehmen
Zielgruppe
VERANSTALTUNGSTECHNIK
Aufgabenstellung
Wir haben diesen Flyer erhalten, finden ihn aber nicht ansprechend, sehr altmodisch und möchten einen klar strukturierten modernen Flyer.
DIN A5 „Heft“ – Und das Profil als „Einleger“. Sollte dementsprechend ca. 1 cm umlaufend kleiner sein.
Der Flyer soll sich an dem Design der Webseite orientieren!

```html
<!DOCTYPE html>
<html lang="de">
<head>
<meta charset="utf-8">
<title>Lumenwerk – Über uns</title>
<link href="https://fonts.googleapis.com/css2?family=Inter:wght@300;400;700&display=swap" rel="stylesheet">
<style>
  :root {
    --purple: #9b82c4;
    --lavender: #e6e2f0;
    --ink: #1d1d1f;
    --white: #ffffff;
    --photo-dark: #0d0d0d;
    --photo-mid: #4a4a4a;
    --photo-light: #d8d8d8;
  }
  * { margin: 0; padding: 0; box-sizing: border-box; }
  html, body { width: 1200px; height: 822px; overflow: hidden; }
  body { font-family: "Inter", Arial, sans-serif; color: var(--ink); position: relative; }

  .page-left {
    position: absolute; left: 0; top: 0; width: 600px; height: 822px;
    background: linear-gradient(to bottom, var(--white) 0%, var(--white) 70%, var(--lavender) 100%);
  }
  .section-tag {
    position: absolute; left: 56px; top: 70px; width: 139px; height: 36px;
    background: var(--purple); border-radius: 5px; color: var(--white);
    font-size: 22px; line-height: 36px; padding-left: 12px; letter-spacing: -0.3px;
  }
  .section-tag strong { font-weight: 700; }
  .section-tag span { font-weight: 300; }

  .about-text {
    position: absolute; left: 56px; top: 126px; width: 492px;
    font-size: 15.6px; line-height: 19.6px; font-weight: 400; letter-spacing: -0.1px;
    hyphens: auto;
  }
  .about-text p + p { margin-top: 15px; }

  .team { position: absolute; left: 0; top: 611px; width: 600px; }
  .member { position: absolute; width: 130px; text-align: center; }
  .portrait {
    width: 101px; height: 101px; margin: 0 auto; border-radius: 50%;
    border: 2px solid var(--purple);
    background: radial-gradient(circle at 50% 40%, #bdbdbd 0%, #8e8e8e 70%, #5e5e5e 100%);
  }
  .member-name { margin-top: 12px; font-size: 13.5px; font-weight: 300; }
  .member-name strong { font-weight: 700; }

  .folio { position: absolute; top: 776px; font-size: 12px; font-weight: 300; }
  .folio-left { left: 40px; color: var(--ink); }
  .folio-right { right: 41px; color: var(--white); }

  .page-right {
    position: absolute; left: 600px; top: 0; width: 600px; height: 822px;
    background: radial-gradient(ellipse 60% 35% at 50% 33%, var(--photo-light) 0%, var(--photo-mid) 45%, #222 75%, var(--photo-dark) 100%);
  }
  .brand-rule { position: absolute; top: 705px; height: 2px; background: var(--white); }
  .brand-rule.left { left: 0; width: 232px; }
  .brand-rule.right { left: 400px; width: 200px; }
  .brand-name {
    position: absolute; left: 232px; width: 168px; top: 693px; text-align: center;
    color: var(--white); font-size: 20px; font-weight: 400; line-height: 26px;
  }
</style>
</head>
<body>
  <section class="page-left">
    <div class="section-tag"><strong>ÜBER</strong> <span>UNS</span></div>

    <div class="about-text">
      <p>Gemeinsam mit Ihnen und nach Ihren Wünschen setzen wir Veranstaltungskonzepte und Ideen um. Wir sorgen für einen reibungslosen Ablauf. 1992 startete die Lumenwerk GmbH als Dienstleister für Film und Fernsehen. Seitdem sorgen wir mit unserer Firmenphilosophie, unseren nachhaltig durchdachten Konzepten und unseren rund 50 Mitarbeiter:innen für Flexibilität, Vertrauen und Transparenz in der Umsetzung Ihrer Projekte.</p>
      <p>Durch unsere Zusammenarbeit mit renommierten Medienhäusern wie Kanal Nord, Sender Mitte, Metropol TV und Rundfunk Ost haben wir Fachkompetenzen im Bereich der TV-Produktionen und Übertragungen von Veranstaltungen.</p>
      <p>Wir bieten flexible Komplettlösungen für Veranstaltungen aller Art und realisieren große Events mit einem Rundum-Service, der mehrere Bereiche des Eventmanagements gleichzeitig abdeckt. Denn neben der Planung und Durchführung bieten wir auch einen umfangreichen Technikverleih und das passende Fachpersonal für Ihre Veranstaltung.</p>
      <p>Unser Event-Team zeichnet sich durch fachliches Know-how aus unterschiedlichen Ausbildungsrichtungen aus und betrachtet Ihre Veranstaltung sowohl aus kaufmännischer als auch aus technischer Sicht mit einem unterstützenden Faktor aus dem Managementbereich.</p>
    </div>

    <div class="team">
      <div class="member" style="left:41px">
        <div class="portrait" role="img" aria-label="Porträtfoto von Jonas Falkner"></div>
        <div class="member-name"><strong>Jonas</strong> Falkner</div>
      </div>
      <div class="member" style="left:170px">
        <div class="portrait" role="img" aria-label="Porträtfoto von Sabine Roth"></div>
        <div class="member-name"><strong>Sabine</strong> Roth</div>
      </div>
      <div class="member" style="left:300px">
        <div class="portrait" role="img" aria-label="Porträtfoto von Mira Albers"></div>
        <div class="member-name"><strong>Mira</strong> Albers</div>
      </div>
      <div class="member" style="left:429px">
        <div class="portrait" role="img" aria-label="Porträtfoto von Lea Kranz"></div>
        <div class="member-name"><strong>Lea</strong> Kranz</div>
      </div>
    </div>

    <div class="folio folio-left">2&nbsp; | &nbsp;Lumenwerk</div>
  </section>

  <section class="page-right" role="img" aria-label="Schwarz-weißes Konzertfoto: Bühne mit hellen Scheinwerfern und Nebel, Publikum mit erhobenen Smartphones im Vordergrund">
    <div class="brand-rule left"></div>
    <div class="brand-name">Lumenwerk</div>
    <div class="brand-rule right"></div>
    <div class="folio folio-right">Lumenwerk&nbsp; | &nbsp;3</div>
  </section>
</body>
</html>
```